Koruvo Martial Art Website Redesign

We have an existing website at www.koruvo.com.au and are looking for a fresh new design for it as it's looking old and cluttered.

When doing the social media icons, we also need one for Vid Stream which we currently don't have on the site.

We are happy with the actual copy and just want a redesign.

It needs to look dark and edgy.

Target Market(s)

People interested in self defence classes and private training

Number of Pages Required

1 page

Font styles to use
Sans Serif

```html
<!DOCTYPE html>
<html lang="en">
<head>
<meta charset="utf-8">
<title>Koruvo Martial Art</title>
<link href="https://fonts.googleapis.com/css2?family=Roboto+Condensed:ital,wght@0,400;0,700;1,700;1,800&family=Roboto:wght@400;500;700&display=swap" rel="stylesheet">
<style>
:root{
  --page:#1c1d21;
  --ink:#121317;
  --ink-2:#0c0d10;
  --red:#b3141b;
  --red-dark:#6e0c10;
  --blue:#2e3b8f;
  --blue-btn:#2b3990;
  --gold:#c49a3a;
  --white:#ffffff;
  --grey-text:#3a3a3a;
  --muted:#9a9ca4;
}
*{box-sizing:border-box;margin:0;padding:0}
html,body{width:1200px;height:2596px;overflow:hidden}
body{background:var(--page);font-family:'Roboto',sans-serif;color:var(--white)}
.site{position:absolute;left:170px;top:18px;width:860px;height:2560px;background:var(--white);overflow:hidden}
section,header,footer{position:relative;width:860px;overflow:hidden}
.cond{font-family:'Roboto Condensed',sans-serif}

/* hero */
.hero{height:430px;background:var(--ink)}
.hero-shapes{position:absolute;inset:0}
.hero-photo{position:absolute;left:390px;top:40px;width:470px;height:360px;background:radial-gradient(ellipse at 55% 45%,#e9ecf2 0%,#8f9bb8 30%,#2c3a6b 55%,transparent 75%)}
.nav{position:absolute;top:0;left:0;width:100%;height:54px;display:flex;align-items:center;padding:0 26px;background:rgba(10,11,14,.9)}
.brand{display:flex;align-items:center;gap:8px;font-family:'Roboto Condensed',sans-serif;font-weight:700;font-size:15px;color:var(--white)}
.brand-dot{width:22px;height:22px;border-radius:50%;background:var(--gold)}
.menu{margin-left:auto;display:flex;gap:14px;font-size:10.5px;color:#d7d8dd}
.menu .active{background:var(--blue-btn);color:#fff;padding:4px 9px;margin:-4px 0}
.hero-title{position:absolute;left:70px;top:88px;font-family:'Roboto Condensed',sans-serif;font-style:italic;font-weight:800;text-transform:uppercase;line-height:.98}
.hero-title span{display:block}
.t1{font-size:46px;margin-left:120px}
.t2{font-size:42px;color:var(--red);margin-left:54px}
.t3{font-size:58px}
.hero-intro{position:absolute;left:70px;top:268px;width:300px;font-size:14px;line-height:1.45;color:#e7e8ec}
.btn{display:inline-block;background:var(--blue-btn);color:#fff;font-size:12px;font-weight:500;padding:9px 26px}
.hero .btn{position:absolute;left:70px;top:345px}

/* intro */
.intro{height:100px;background:var(--white);color:var(--grey-text)}
.call{position:absolute;right:24px;top:-2px;background:var(--blue-btn);color:#fff;font-size:11px;padding:7px 14px;display:flex;gap:6px;align-items:center}
.intro p{position:absolute;left:190px;top:34px;width:480px;text-align:center;font-size:12.5px;line-height:1.55}

/* training */
.training{height:410px;background:var(--white)}
.training-photo{position:absolute;left:330px;top:36px;width:490px;height:300px;background:linear-gradient(120deg,#f2f2f2 0%,#9b9b9b 45%,#2a2a2a 75%,#bdbdbd 100%)}
.training-card{position:absolute;left:60px;top:60px;width:340px;height:260px}
.training-card h2{position:absolute;left:52px;top:72px;font-family:'Roboto Condensed',sans-serif;font-weight:800;font-style:italic;font-size:34px;line-height:1.05;color:#fff;text-transform:uppercase}
.dots{position:absolute;left:400px;top:356px;display:flex;gap:10px}
.dots span{width:18px;height:18px;border-radius:50%;border:1.5px solid #555;display:flex;align-items:center;justify-content:center}

/* blue band */
.band{height:225px;background:var(--blue);padding:28px 70px}
.band p{font-size:12px;line-height:1.6;color:#e6e8f5;margin-bottom:12px}

/* mission */
.mission{height:460px;background:var(--white)}
.kick-photo{position:absolute;left:40px;top:20px;width:360px;height:420px;background:radial-gradient(ellipse at 50% 50%,#e4e4e4 0%,#bfbfbf 35%,#fff 70%)}
.gold-box{position:absolute;left:440px;top:50px;width:380px;height:300px;background:var(--gold);padding:34px 30px;font-size:12.5px;line-height:1.6;color:#fff}
.gold-box p{margin-bottom:14px}
.gold-box .sign{font-style:italic;font-size:11.5px}

/* testimonial */
.said{height:230px;background:linear-gradient(90deg,var(--red) 0%,var(--red-dark) 45%,var(--ink) 80%)}
.said h2{position:absolute;left:70px;top:30px;font-family:'Roboto Condensed',sans-serif;font-weight:800;font-style:italic;font-size:38px;text-transform:uppercase}
.said blockquote{position:absolute;left:70px;top:92px;width:450px;font-size:12.5px;line-height:1.6}
.said cite{position:absolute;left:70px;top:178px;font-size:11.5px;font-style:italic}
.said-figure{position:absolute;right:60px;top:25px;width:190px;height:190px;background:radial-gradient(circle,#1c0607 0%,#3a0a0c 50%,transparent 72%)}

/* register */
.register{height:380px;background:var(--ink);text-align:center}
.register h2{padding-top:30px;font-family:'Roboto Condensed',sans-serif;font-weight:800;font-style:italic;font-size:34px;text-transform:uppercase}
.register h3{font-family:'Roboto Condensed',sans-serif;font-weight:700;font-size:13px;letter-spacing:.5px;margin-top:2px}
.form{position:absolute;left:100px;top:110px;width:660px;display:grid;grid-template-columns:1fr 1fr;gap:9px 16px}
.field{height:26px;background:#fff;color:#777;font-size:10.5px;text-align:left;padding:6px 10px}
.field.wide{grid-column:1/3}
.register .btn{position:absolute;left:370px;top:322px;width:120px;text-align:center}

/* footer */
.footer{height:325px;background:var(--ink-2);color:var(--muted);font-size:10.5px}
.foot-line{position:absolute;left:0;top:18px;width:100%;text-align:center;font-size:10px}
.cols{position:absolute;left:60px;top:60px;width:740px;display:grid;grid-template-columns:1fr 1fr 1fr;gap:30px}
.cols h4{color:#fff;font-size:12px;font-weight:500;line-height:1.35;margin-bottom:8px}
.cols p{line-height:1.55;margin-bottom:10px}
.small-btn{display:inline-block;background:var(--blue-btn);color:#fff;padding:5px 14px;font-size:10px}
.news .input{height:22px;background:#fff;color:#777;padding:5px 8px;margin-bottom:7px;font-size:10px}
.socials{display:flex;gap:8px;margin-top:10px}
.socials span{width:20px;height:20px;border-radius:50%;background:#4a4c55}
.copy{position:absolute;left:0;top:262px;width:100%;text-align:center;font-size:10px}
.copy div{margin-top:5px}
.book{position:absolute;right:60px;top:258px}
</style>
</head>
<body>
<div class="site">

<header class="hero">
  <div class="hero-photo" role="img" aria-label="Photo of two martial artists in white and blue uniforms performing a throw"></div>
  <svg class="hero-shapes" width="860" height="430" viewBox="0 0 860 430" aria-hidden="true">
    <polygon points="700,250 860,170 860,430 640,430" fill="var(--red)"/>
    <polygon points="0,300 40,280 40,430 0,430" fill="var(--blue)"/>
  </svg>
  <nav class="nav">
    <div class="brand"><span class="brand-dot"></span>Koruvo Martial Art</div>
    <div class="menu"><span class="active">Home</span><span>About Us</span><span>Styles</span><span>Locations</span><span>Instructors</span><span>Curriculum</span><span>Gallery</span><span>Membership</span><span>Blog</span><span>Contact Us</span></div>
  </nav>
  <h1 class="hero-title"><span class="t1">Learn Fast</span><span class="t2">Powerful “Street”</span><span class="t3">Self-Defence</span></h1>
  <p class="hero-intro">Welcome to Koruvo Martial Art. We are excited for the opportunity to share this amazing art with you.</p>
  <a class="btn">Join Us</a>
</header>

<section class="intro">
  <div class="call"><svg width="10" height="10" viewBox="0 0 24 24"><path d="M6.6 10.8a15 15 0 0 0 6.6 6.6l2.2-2.2a1 1 0 0 1 1-.25 11 11 0 0 0 3.6.6 1 1 0 0 1 1 1V20a1 1 0 0 1-1 1A17 17 0 0 1 3 4a1 1 0 0 1 1-1h3.5a1 1 0 0 1 1 1 11 11 0 0 0 .6 3.6 1 1 0 0 1-.25 1z" fill="#fff"/></svg>Call Us Today</div>
  <p>Koruvo Martial Art is a fast, powerful, dynamic and “street” effective self-defence style that teaches efficient, practical and easily adaptable techniques for the modern world.</p>
</section>

<section class="training">
  <div class="training-photo" role="img" aria-label="Black and white photo of an instructor demonstrating a strike"></div>
  <div class="training-card">
    <svg width="340" height="260" viewBox="0 0 340 260" aria-hidden="true"><polygon points="60,0 340,0 280,260 0,260" fill="var(--red)"/></svg>
    <h2>One on One<br>Private<br>Training</h2>
  </div>
  <div class="dots">
    <span><svg width="8" height="8" viewBox="0 0 8 8"><path d="M5.5 1 2.5 4l3 3" stroke="#555" fill="none" stroke-width="1.4"/></svg></span>
    <span><svg width="8" height="8" viewBox="0 0 8 8"><path d="M2.5 1l3 3-3 3" stroke="#555" fill="none" stroke-width="1.4"/></svg></span>
  </div>
</section>

<section class="band">
  <p>Our one on one private sessions are built around your goals, your pace and your schedule so every minute of training counts.</p>
  <p>You will learn to move with confidence, react under pressure and protect yourself and the people you care about most.</p>
  <p>Each lesson blends striking, grappling and awareness drills with honest feedback from an experienced instructor who trains alongside you.</p>
  <p>Sessions run across the week at a time that suits you, and your very first private lesson is completely free.</p>
</section>

<section class="mission">
  <div class="kick-photo" role="img" aria-label="Photo of a martial artist in a white uniform performing a high kick"></div>
  <div class="gold-box">
    <p>Koruvo combines the practical aspects of many martial arts into one direct and efficient system built for real situations today.</p>
    <p>In the time that it takes to learn one technique elsewhere, students here gain skills they can use straight away.</p>
    <p class="sign">Marcus Hale, Chief Instructor</p>
  </div>
</section>

<section class="said">
  <h2>What They Said</h2>
  <blockquote>Koruvo Martial Art is giving me the confidence to believe that I could look after myself if I ever had to in a dark, quiet carpark. I feel so much stronger and calmer already.</blockquote>
  <cite>Leanne Corbett</cite>
  <div class="said-figure" role="img" aria-label="Silhouette of a martial artist mid kick"></div>
</section>

<section class="register">
  <h2>Register Below</h2>
  <h3>FOR A COMPLIMENTARY PRIVATE LESSON</h3>
  <div class="form">
    <div class="field">First Name</div><div class="field">Last Name</div>
    <div class="field">Email</div><div class="field">Phone</div>
    <div class="field">Suburb</div><div class="field">Preferred Location</div>
    <div class="field wide">Preferred Time</div>
    <div class="field wide" style="height:60px">Message</div>
  </div>
  <a class="btn">Register</a>
</section>

<footer class="footer">
  <div class="foot-line">Koruvo Martial Art · Private Lessons · Self Defence Classes · www.koruvo.com.au</div>
  <div class="cols">
    <div>
      <h4>Every Fighting Style Explained for Beginners</h4>
      <p>A quick guide to the core ideas behind each style we teach and how they fit together.</p>
      <span class="small-btn">Read More</span>
    </div>
    <div>
      <h4>Weekly Drills to Sharpen Your Reaction Speed</h4>
      <p>Simple routines you can practise at home between classes to stay sharp and ready.</p>
      <span class="small-btn">Read More</span>
    </div>
    <div class="news">
      <h4>Subscribe to our Newsletter</h4>
      <div class="input">Your Name</div>
      <div class="input">Your Email</div>
      <span class="small-btn">Subscribe</span>
      <div class="socials" aria-label="Social links including Vid Stream"><span></span><span></span><span></span><span></span></div>
    </div>
  </div>
  <div class="copy">© 2024 Koruvo Martial Art. All rights reserved.<div>www.koruvo.com.au</div></div>
  <span class="small-btn book">Book a Free Lesson</span>
</footer>

</div>
</body>
</html>
```